Ombrik Partnering Business Card

Hello everyone. We need a business card design that would match our logo and the theme we're trying to have for Ombrik that you can find on our website and/or Linkedin page

```html
<!DOCTYPE html>
<html lang="en">
<head>
<meta charset="UTF-8">
<title>Ombrik Partnering Business Card</title>
<link rel="stylesheet" href="https://fonts.googleapis.com/css2?family=Poppins:wght@400;600&display=swap">
<style>
  :root {
    --stage: #232326;
    --navy: #182a57;
    --white: #ffffff;
    --purple: #33205e;
    --teal: #1aa89a;
    --gold: #f0b92a;
    --lilac: #8d8fb3;
  }
  * { margin: 0; padding: 0; box-sizing: border-box; }
  html, body { width: 1200px; height: 864px; overflow: hidden; }
  body {
    background: var(--stage);
    font-family: "Poppins", sans-serif;
    position: relative;
  }
  .card {
    position: absolute;
    width: 540px;
    height: 310px;
    border-radius: 22px;
    overflow: hidden;
  }

  .brand {
    position: absolute;
    display: flex;
    align-items: center;
    gap: 12px;
    font-weight: 600;
    white-space: nowrap;
    line-height: 1;
  }
  .brand-dot {
    border-radius: 50%;
    background: currentColor;
    flex: none;
  }

  /* Back side */
  .card-back {
    left: 60px;
    top: 90px;
    background: var(--navy);
  }
  .card-back .brand {
    left: 0;
    right: 0;
    top: 136px;
    justify-content: center;
    color: var(--white);
    font-size: 34px;
  }
  .card-back .brand-dot { width: 16px; height: 16px; }
  .social-handle {
    position: absolute;
    right: 34px;
    bottom: 26px;
    display: flex;
    align-items: center;
    gap: 6px;
    color: var(--white);
    font-size: 12px;
  }
  .social-square {
    width: 11px;
    height: 11px;
    background: var(--white);
    border-radius: 2px;
  }

  /* Front side */
  .card-front {
    left: 600px;
    top: 470px;
    background: linear-gradient(90deg, var(--white) 0%, var(--white) 40%, var(--lilac) 46%, var(--navy) 52%, var(--navy) 100%);
  }
  .wave-band {
    position: absolute;
    left: 236px;
    top: 0;
    width: 90px;
    height: 310px;
    background: linear-gradient(90deg, rgba(26,168,154,0) 0%, rgba(26,168,154,0.85) 22%, rgba(255,255,255,0.8) 50%, rgba(240,185,42,0.9) 78%, rgba(240,185,42,0) 100%);
  }
  .card-front .brand {
    left: 22px;
    top: 145px;
    color: var(--purple);
    font-size: 20px;
    gap: 9px;
  }
  .card-front .brand-dot { width: 11px; height: 11px; }
  .contact {
    position: absolute;
    right: 28px;
    top: 98px;
    text-align: right;
    color: var(--white);
  }
  .contact-name {
    font-size: 18px;
    font-weight: 600;
    margin-bottom: 8px;
  }
  .contact-line {
    display: flex;
    justify-content: flex-end;
    align-items: center;
    gap: 8px;
    font-size: 12px;
    line-height: 22px;
  }
  .contact-icon { width: 13px; height: 13px; flex: none; }
</style>
</head>
<body>

  <section class="card card-back" aria-label="Card back">
    <div class="brand"><span class="brand-dot"></span>Ombrik Partnering</div>
    <div class="social-handle"><span class="social-square"></span>: ombrikpartnering</div>
  </section>

  <section class="card card-front" aria-label="Card front">
    <div class="wave-band" role="img" aria-label="Flowing bands of fine teal, white and gold lines sweeping across the card"></div>
    <div class="brand"><span class="brand-dot"></span>Ombrik Partnering</div>
    <div class="contact">
      <p class="contact-name">Daniel Hartley</p>
      <p class="contact-line">0412 638 207
        <svg class="contact-icon" viewBox="0 0 16 16"><rect width="16" height="16" rx="3" fill="#f0b92a"/><path d="M4 4h3l1 3-2 1a7 7 0 0 0 2 2l1-2 3 1v3c-5 0-8-3-8-8z" fill="#182a57"/></svg>
      </p>
      <p class="contact-line">info@ombrikpartnering.com
        <svg class="contact-icon" viewBox="0 0 16 16"><rect width="16" height="16" rx="3" fill="#f0b92a"/><rect x="3" y="5" width="10" height="7" fill="none" stroke="#182a57" stroke-width="1.4"/><path d="M3 5l5 4 5-4" fill="none" stroke="#182a57" stroke-width="1.4"/></svg>
      </p>
      <p class="contact-line">www.ombrikpartnering.com
        <svg class="contact-icon" viewBox="0 0 16 16"><circle cx="8" cy="8" r="7" fill="#f0b92a"/><circle cx="8" cy="8" r="4.5" fill="none" stroke="#182a57" stroke-width="1.2"/><path d="M3.5 8h9M8 3.5v9" stroke="#182a57" stroke-width="1.2"/></svg>
      </p>
    </div>
  </section>

</body>
</html>
```